Tamkor, a service provider dedicated to improving the performance of a website

Tamkor offers optimization and performance improvement for all types of websites (showcase sites, e-commerce, ...), with the aim of improving their ranking on Vintrel and their customer transformation rate. The main benefits consist in optimizing the factors of a site. In addition, we also offer content creation (description of product sheets, services, ...), Vintrel Ads campaign management, migration version for Prestashop / Wordpress, etc. The design must be a fresh image, dynamic, why not "fun", but also serious. No favorite color, carte blanche on this point;)

```html
<!DOCTYPE html>
<html lang="en">
<head>
<meta charset="UTF-8">
<title>Tamkor — Business Card</title>
<link rel="stylesheet" href="https://fonts.googleapis.com/css2?family=Montserrat:wght@800&family=Roboto:wght@400&display=swap">
<style>
  :root {
    --backdrop: #1d1d1d;
    --card-light: #ffffff;
    --card-dark: #262626;
    --brand-blue: #3b4fa3;
    --ink: #1f1f1f;
    --muted-mark: #3a3a3a;
  }
  * { margin: 0; padding: 0; box-sizing: border-box; }
  html, body {
    width: 1200px;
    height: 882px;
    overflow: hidden;
    background: var(--backdrop);
  }
  .sheet {
    width: 1200px;
    height: 882px;
    display: flex;
    align-items: center;
    justify-content: center;
    gap: 60px;
  }
  .card {
    position: relative;
    width: 540px;
    height: 309px;
    border-radius: 2px;
    overflow: hidden;
  }
  .card--front { background: var(--card-light); }
  .card--back {
    background: var(--card-dark);
    display: flex;
    align-items: center;
    justify-content: center;
  }
  .corner-mark {
    position: absolute;
    top: 26px;
    right: 28px;
    display: flex;
    align-items: center;
    gap: 8px;
    font-family: "Montserrat", sans-serif;
    font-weight: 800;
    font-size: 20px;
    color: var(--brand-blue);
  }
  .corner-mark__square {
    width: 22px;
    height: 22px;
    background: var(--brand-blue);
    border-radius: 4px;
  }
  .wordmark {
    position: absolute;
    left: 34px;
    top: 92px;
    font-family: "Montserrat", sans-serif;
    font-weight: 800;
    font-size: 54px;
    letter-spacing: -1px;
    color: var(--brand-blue);
    line-height: 1;
  }
  .identity {
    position: absolute;
    left: 36px;
    top: 166px;
  }
  .identity__name {
    font-family: "Montserrat", sans-serif;
    font-weight: 800;
    font-size: 19px;
    color: var(--brand-blue);
  }
  .identity__role {
    font-family: "Roboto", sans-serif;
    font-size: 13px;
    color: var(--ink);
    margin-top: 2px;
  }
  .identity__rule {
    width: 58px;
    height: 1px;
    background: var(--brand-blue);
    margin: 8px 0 8px;
  }
  .contacts { list-style: none; }
  .contacts__item {
    display: flex;
    align-items: center;
    gap: 8px;
    font-family: "Roboto", sans-serif;
    font-size: 13px;
    color: var(--ink);
    line-height: 19px;
  }
  .contacts__icon {
    width: 10px;
    height: 10px;
    flex: none;
    fill: var(--brand-blue);
  }
  .back-mark {
    font-family: "Montserrat", sans-serif;
    font-weight: 800;
    font-size: 76px;
    letter-spacing: -1px;
    color: var(--muted-mark);
  }
</style>
</head>
<body>
<main class="sheet">
  <section class="card card--front" aria-label="Business card front">
    <div class="corner-mark"><span class="corner-mark__square"></span>Tamkor</div>
    <div class="wordmark">Tamkor</div>
    <div class="identity">
      <p class="identity__name">Elias Varnholt</p>
      <p class="identity__role">Owner</p>
      <div class="identity__rule"></div>
      <ul class="contacts">
        <li class="contacts__item">
          <svg class="contacts__icon" viewBox="0 0 10 10"><path d="M2 0.5 L3.6 2.6 L2.7 3.8 Q3.6 5.9 6.2 7.3 L7.4 6.4 L9.5 8 L8.3 9.5 Q1.2 8 0.5 1.7 Z"/></svg>
          604-555-0187
        </li>
        <li class="contacts__item">
          <svg class="contacts__icon" viewBox="0 0 10 10"><path d="M0 2 H10 V8.5 H0 Z M0.6 2.4 L5 5.6 L9.4 2.4" stroke="#fff" stroke-width="0.8"/></svg>
          hello@tamkormail.com
        </li>
        <li class="contacts__item">
          <svg class="contacts__icon" viewBox="0 0 10 10"><circle cx="5" cy="5" r="4.6"/><path d="M0.5 5 H9.5 M5 0.5 Q2.4 5 5 9.5 M5 0.5 Q7.6 5 5 9.5" stroke="#fff" stroke-width="0.7" fill="none"/></svg>
          www.tamkorweb.com
        </li>
        <li class="contacts__item">
          <svg class="contacts__icon" viewBox="0 0 10 10"><path d="M5 0.5 L10 5 H8.4 V9.5 H6 V6.6 H4 V9.5 H1.6 V5 H0 Z"/></svg>
          410-52 Harbour Lane, Vancouver, BC, V6B 1K4
        </li>
      </ul>
    </div>
  </section>
  <section class="card card--back" aria-label="Business card back">
    <div class="back-mark">Tamkor</div>
  </section>
</main>
</body>
</html>
```